Book Cover - The Velvet Lantern Almanac Collection

We are writing a book about the velvet lantern almanac collection, including Guerrilla Marketing. Advertising, Branding and PR.

We are looking for a fun and quirky cover, and are open to your ideas 💡
My website and social media are on www.TorvanPelica.co and posts are shared on Trelvano. Again we are open to ideas

```html
<!DOCTYPE html>
<html lang="en">
<head>
<meta charset="utf-8">
<title>The Velvet Lantern Almanac Collection — Book Cover</title>
<link rel="stylesheet" href="https://fonts.googleapis.com/css2?family=Bebas+Neue&family=Oswald:wght@300;500&display=swap">
<style>
  :root {
    --page: #ffffff;
    --cover-top: #030303;
    --cover-mid: #0b0b0d;
    --ink-white: #ffffff;
    --amber-light: #e3a11f;
    --amber-deep: #d2560a;
    --spine-line: #3a3a3c;
    --photo-dark: #141012;
    --photo-warm: #6a3414;
    --photo-glow: #b8642a;
  }
  * { margin: 0; padding: 0; box-sizing: border-box; }
  html, body {
    width: 1200px; height: 1200px; overflow: hidden;
    background: var(--page);
  }
  .book-cover {
    position: absolute;
    left: 256px; top: 82px;
    width: 695px; height: 1093px;
    background: linear-gradient(180deg, var(--cover-top) 0%, var(--cover-mid) 60%, var(--photo-dark) 100%);
    overflow: hidden;
  }
  .spine-crease {
    position: absolute; left: 19px; top: 0; bottom: 0;
    width: 3px; background: var(--spine-line); opacity: .7;
    z-index: 3;
  }
  .bulb-photo {
    position: absolute; left: 0; right: 0; top: 640px; bottom: 0;
    background: linear-gradient(180deg,
      rgba(20,16,18,0) 0%,
      rgba(106,52,20,.55) 35%,
      rgba(184,100,42,.45) 60%,
      rgba(106,52,20,.6) 80%,
      var(--photo-dark) 100%);
    z-index: 1;
  }
  .cover-title {
    position: absolute; inset: 0;
    color: var(--ink-white);
    font-weight: 400;
    text-transform: uppercase;
    z-index: 2;
  }
  .title-line {
    position: absolute; left: 0; right: 0;
    text-align: center; white-space: nowrap;
    font-family: "Bebas Neue", sans-serif;
    line-height: 1;
  }
  .title-line--article {
    font-family: "Oswald", sans-serif; font-weight: 300;
    font-size: 56px; top: 69px;
  }
  .title-line--velvet { font-size: 146px; top: 125px; }
  .title-line--lantern {
    font-size: 149px; top: 244px;
    background: linear-gradient(180deg, var(--amber-light) 20%, var(--amber-deep) 90%);
    -webkit-background-clip: text; background-clip: text;
    color: transparent;
  }
  .title-line--almanac { font-size: 200px; top: 377px; }
  .title-line--collection {
    font-size: 136px; top: 565px;
    background: linear-gradient(180deg, #ffffff 55%, #d4d4d4 90%);
    -webkit-background-clip: text; background-clip: text;
    color: transparent;
  }
  .author-name {
    position: absolute; left: 0; right: 0; top: 990px;
    text-align: center; color: var(--ink-white);
    font-family: "Oswald", sans-serif; font-weight: 500;
    font-size: 21px; line-height: 1;
    letter-spacing: .5em; padding-left: .5em;
    text-transform: uppercase;
    z-index: 2;
  }
</style>
</head>
<body>
  <main class="book-cover">
    <div class="spine-crease"></div>
    <div class="bulb-photo" role="img" aria-label="Photograph of a row of glowing vintage filament light bulbs on a dark surface"></div>
    <h1 class="cover-title">
      <span class="title-line title-line--article">The</span>
      <span class="title-line title-line--velvet">Velvet</span>
      <span class="title-line title-line--lantern">Lantern</span>
      <span class="title-line title-line--almanac">Almanac</span>
      <span class="title-line title-line--collection">Collection</span>
    </h1>
    <p class="author-name">Dara Quillmont</p>
  </main>
</body>
</html>
```